Upgrade/"Tweak" My Landing Page

We need to "tweak" our current landing page. I'm a perfectionist and something seems "off". Things I LOVE about our current page: I love our message that "ONE SIZE DOES NOT FIT ALL", as well as the photo used (boy wearing an oversized hat). I also like the fact that the photo is in full screen mode- I like this look.
THINGS I DON'T Like: The font & location of our message "ONE SIZE DOES NOT FIT ALL" - just seems "off". I'm also concerned about the placement of our menu being on the left hand side of the screen. Not sure if this is ideal. Also, my product types are listed on the left hand side of the screen in the menu section. My audience seems to think these are links when in fact they are just examples of the products I sell. How can I position these so the audience knows it's for informational purposes only.
Help!! I want my landing page to be PERFECT.

```html
<!DOCTYPE html>
<html lang="en">
<head>
<meta charset="utf-8">
<title>Harborline Insurance Agency</title>
<link rel="stylesheet" href="https://fonts.googleapis.com/css2?family=Open+Sans:wght@600&family=Oswald:wght@300;400&family=Roboto:wght@300;400;500;700&family=Roboto+Condensed:wght@400&display=swap">
<style>
  :root {
    --navy: #1d2f63;
    --nav-blue: #4a6592;
    --nav-blue-dark: #3f5783;
    --sky-top: #5b8ad6;
    --sky-bottom: #a3c2ec;
    --accent-red: #e8354f;
    --phone-pink: #ee5a70;
    --icon-grey: #9a9a9a;
    --band-grey: #f5f5f5;
    --rule: #dddddd;
    --city-dark: #171d2b;
    --city-mid: #3d4c6e;
    --white: #ffffff;
    --muted: #777777;
  }
  * { margin: 0; padding: 0; box-sizing: border-box; }
  html, body { width: 1200px; height: 1000px; overflow: hidden; background: var(--white); }
  body { position: relative; font-family: "Roboto", Arial, sans-serif; }

  .site-header { position: absolute; top: 0; left: 0; width: 1200px; height: 110px; display: flex; flex-direction: column; align-items: center; justify-content: center; gap: 8px; }
  .brand-mark { width: 22px; height: 22px; border-radius: 50%; background: var(--navy); }
  .brand-name { font-family: "Roboto", Arial, sans-serif; font-weight: 700; font-size: 15px; letter-spacing: 0.5px; color: var(--navy); text-align: center; line-height: 1.25; }

  .main-nav { position: absolute; top: 110px; left: 0; width: 1200px; height: 40px; background: linear-gradient(var(--nav-blue), var(--nav-blue-dark)); display: flex; justify-content: center; align-items: center; padding-bottom: 3px; }
  .main-nav a { font-family: "Open Sans", Arial, sans-serif; font-weight: 600; font-size: 11.5px; color: var(--white); text-decoration: none; }
  .main-nav .sep { color: var(--white); font-size: 11px; margin: 0 15px; }

  .hero { position: absolute; top: 150px; left: 0; width: 1200px; height: 413px; }
  .hero-photo { position: absolute; inset: 0; background: linear-gradient(180deg, var(--sky-top) 0%, var(--sky-bottom) 100%); }
  .social { position: absolute; top: 8px; left: 898px; display: flex; gap: 6px; }
  .social span { width: 24px; height: 24px; background: #3b5fa8; display: block; }
  .social span + span { background: #1e88c8; }
  .hero-copy { position: absolute; top: 268px; left: 0; width: 1200px; text-align: center; color: var(--white); }
  .hero-title { font-family: "Oswald", "Arial Narrow", sans-serif; font-weight: 300; font-size: 62px; line-height: 68px; letter-spacing: -1px; transform: scaleX(0.7); text-shadow: 0 1px 4px rgba(0,0,0,0.25); }
  .hero-sub { font-family: "Roboto", Arial, sans-serif; font-weight: 700; font-size: 21.5px; line-height: 24px; margin-top: -6px; text-shadow: 0 1px 3px rgba(0,0,0,0.3); }
  .hero-button { display: inline-block; margin-top: 13px; width: 107px; height: 26px; border: 1.5px solid var(--white); color: var(--white); font-size: 14px; line-height: 23px; text-decoration: none; background: rgba(0,0,0,0.05); }

  .products-head { position: absolute; top: 563px; left: 0; width: 1200px; height: 80px; background: var(--band-grey); border-bottom: 1px solid var(--rule); text-align: center; font-weight: 300; font-size: 21.5px; line-height: 84px; color: var(--muted); }
  .products { position: absolute; top: 666px; left: 238px; display: flex; list-style: none; }
  .product { height: 77px; border-left: 1px solid var(--rule); display: flex; flex-direction: column; align-items: center; }
  .product:first-child { border-left: none; }
  .product-name { font-size: 10.5px; font-weight: 500; line-height: 10px; color: var(--accent-red); text-align: center; height: 45px; padding-top: 3px; }
  .product svg { width: 26px; height: 26px; fill: none; stroke: var(--icon-grey); stroke-width: 2; }
  .product svg .solid { fill: var(--icon-grey); stroke: none; }

  .contact-band { position: absolute; top: 762px; left: 0; width: 1200px; height: 168px; background: var(--city-dark); }
  .city-photo { position: absolute; top: 0; left: 175px; width: 850px; height: 168px; background: linear-gradient(90deg, var(--city-dark) 0%, var(--city-mid) 20%, #4d5d80 50%, var(--city-mid) 80%, var(--city-dark) 100%); }
  .contact-copy { position: absolute; top: 43px; left: 0; width: 1200px; text-align: center; color: var(--white); font-weight: 300; font-size: 16px; line-height: 23px; }
  .phones { margin-top: 14px; font-size: 22px; color: var(--phone-pink); display: flex; justify-content: center; align-items: center; gap: 10px; }
  .phones svg { width: 22px; height: 22px; fill: none; stroke: var(--white); stroke-width: 1.6; }
  .phones .slash { color: var(--white); }

  .site-footer { position: absolute; top: 930px; left: 0; width: 1200px; height: 70px; text-align: center; font-family: "Roboto Condensed", Arial, sans-serif; font-size: 9.5px; }
  .footer-links { margin-top: 24px; color: var(--navy); }
  .footer-links a { color: var(--navy); text-decoration: none; }
  .copyright { margin-top: 4px; color: var(--muted); }
</style>
</head>
<body>
  <header class="site-header">
    <span class="brand-mark"></span>
    <div class="brand-name">HARBORLINE INSURANCE<br>AGENCY</div>
  </header>

  <nav class="main-nav">
    <a href="#">About us</a><span class="sep">|</span>
    <a href="#">Pay your bill</a><span class="sep">|</span>
    <a href="#">Request a quote or policy change</a><span class="sep">|</span>
    <a href="#">File a claim</a><span class="sep">|</span>
    <a href="#">Contact us</a>
  </nav>

  <section class="hero">
    <div class="hero-photo" role="img" aria-label="Full-width photo of a child seen from behind wearing an oversized red sun hat against a clear blue sky"></div>
    <div class="social"><span></span><span></span></div>
    <div class="hero-copy">
      <h1 class="hero-title">ONE SIZE DOES NOT FIT ALL</h1>
      <p class="hero-sub">Custom-made solutions at your fingertips</p>
      <a class="hero-button" href="#">KNOW MORE</a>
    </div>
  </section>

  <h2 class="products-head">Our Insurance Products</h2>
  <ul class="products">
    <li class="product" style="width:66px"><span class="product-name">HOME</span>
      <svg viewBox="0 0 26 26"><path class="solid" d="M2 13 13 3l11 10h-3v11h-6v-7h-4v7H5V13z"/></svg></li>
    <li class="product" style="width:67px"><span class="product-name">CONDO</span>
      <svg viewBox="0 0 26 26"><rect class="solid" x="7" y="1" width="13" height="24"/><g fill="#fff"><rect x="9" y="4" width="3" height="3"/><rect x="15" y="4" width="3" height="3"/><rect x="9" y="10" width="3" height="3"/><rect x="15" y="10" width="3" height="3"/><rect x="9" y="16" width="3" height="3"/><rect x="15" y="16" width="3" height="3"/></g></svg></li>
    <li class="product" style="width:78px"><span class="product-name">BUSINESS</span>
      <svg viewBox="0 0 26 26"><rect class="solid" x="3" y="8" width="20" height="15" rx="2"/><path d="M9 8V5h8v3"/></svg></li>
    <li class="product" style="width:94px"><span class="product-name">WINDSTORM</span>
      <svg viewBox="0 0 26 26"><path class="solid" d="M6 15a5 5 0 0 1 2-9 6 6 0 0 1 11 2 4 4 0 0 1 0 7z"/><path d="M8 19h12M11 23h10" stroke-width="1.5"/></svg></li>
    <li class="product" style="width:60px"><span class="product-name">FLOOD</span>
      <svg viewBox="0 0 26 26"><path class="solid" d="M6 13 13 6l7 7h-2v3H8v-3z"/><path d="M3 19q2.5-2 5 0t5 0 5 0 5 0M3 23q2.5-2 5 0t5 0 5 0 5 0" stroke-width="1.5"/></svg></li>
    <li class="product" style="width:54px"><span class="product-name">CAR</span>
      <svg viewBox="0 0 26 26"><path d="M3 19v-5l3-6h14l3 6v5z"/><circle class="solid" cx="8" cy="20" r="2.5"/><circle class="solid" cx="18" cy="20" r="2.5"/></svg></li>
    <li class="product" style="width:61px"><span class="product-name">BOAT</span>
      <svg viewBox="0 0 26 26"><path class="solid" d="M13 3v15H6zM14 6l6 12h-6z"/><path class="solid" d="M2 19h22l-3 4H5z"/></svg></li>
    <li class="product" style="width:101px"><span class="product-name">MOTORCYCLE</span>
      <svg viewBox="0 0 26 26" style="width:36px"><circle cx="5" cy="18" r="4"/><circle cx="21" cy="18" r="4"/><path class="solid" d="M8 12h7l3-3h3l-2 5h-3l-3 4H9z"/></svg></li>
    <li class="product" style="width:146px"><span class="product-name">PERSONAL UMBRELLA<br>POLICY</span>
      <svg viewBox="0 0 26 26"><path class="solid" d="M2 12a11 9 0 0 1 22 0z"/><path d="M13 12v9a2 2 0 0 1-4 0" stroke-width="1.5"/></svg></li>
  </ul>

  <section class="contact-band">
    <div class="city-photo" role="img" aria-label="Aerial photo of a downtown skyline of tall buildings in dark blue tones"></div>
    <div class="contact-copy">
      <p>If you are looking for a team that is highly experienced and knowledgeable, and<br>one who will be honest with you about your insurance needs, let’s talk!</p>
      <p class="phones">
        <svg viewBox="0 0 24 24"><circle cx="12" cy="12" r="10"/><path d="M8.5 7.5l2 2-1 1.5q1 2 3.5 3.5l1.5-1 2 2-1.5 1.5q-4 0-7.5-5.5z"/></svg>
        <span>877.555.0142</span><span class="slash">/</span><span>281.555.0176</span>
      </p>
    </div>
  </section>

  <footer class="site-footer">
    <p class="footer-links"><a href="#">Home</a> / <a href="#">About us</a> / <a href="#">Pay your bill</a> / <a href="#">Request a quote or policy change</a> / <a href="#">File a claim</a> / <a href="#">Contact us</a></p>
    <p class="copyright">© Harborline Insurance Agency, 2015. All rights reserved.</p>
  </footer>
</body>
</html>
```